Brambleway Farming

We need a logo design for a new company based in Kelowna, BC. We grow market garden vegetables for sale at market and in a CSA program. We try to only use hand tools for all aspects of cultivating, seeding, weeding, harvesting and distributing. For this reason we consider ourselves very low impact on the environment.

We would like blues and green in the design with an earthy, natural feel

Target Market(s)

Environmentally aware, health conscience

Industry/Entity Type

Farming

Requirements
Must have
• Foot prints with section for contact details all on the one side
Should not have
• Dark, black colours or anything that looks unnatural

```html
<!DOCTYPE html>
<html lang="en">
<head>
<meta charset="utf-8">
<title>Brambleway Farming – Business Card</title>
<link rel="stylesheet" href="https://fonts.googleapis.com/css2?family=Montserrat:wght@300;400;600;700&display=swap">
<style>
  :root {
    --backdrop: #dcdcdc;
    --card: #ffffff;
    --band: #5a9a8c;
    --band-line: #78b0a4;
    --strip: #e6ece8;
    --ink: #2f3b36;
    --muted: #9aa8a2;
    --text: #3f4a45;
    --orange: #e0874a;
    --blue: #3a9fd6;
    --green: #8fc33c;
    --leaf: #7fb84e;
  }
  * { margin: 0; padding: 0; box-sizing: border-box; }
  html, body {
    width: 1200px; height: 800px; overflow: hidden;
    background: var(--backdrop);
    font-family: "Montserrat", sans-serif;
  }
  .canvas {
    width: 1200px; height: 800px;
    display: flex; align-items: center; justify-content: center;
  }
  .card {
    position: relative;
    width: 900px; height: 514px;
    background: var(--card);
    box-shadow: 0 14px 40px rgba(0,0,0,.14);
    overflow: hidden;
  }
  .side-band {
    position: absolute; left: 0; top: 0; bottom: 0;
    width: 150px; background: var(--band);
  }
  .identity { position: absolute; left: 190px; top: 118px; }
  .identity .name {
    font-weight: 700; font-size: 38px; letter-spacing: .5px;
    color: var(--ink); line-height: 1;
  }
  .identity .role {
    font-weight: 300; font-size: 24px; letter-spacing: 1px;
    color: var(--muted); margin-top: 4px;
  }
  .contacts { position: absolute; left: 0; top: 232px; width: 620px; }
  .contact-row {
    position: relative; height: 72px; margin-bottom: 6px;
    display: flex; align-items: stretch;
  }
  .contact-row .icon-cell {
    width: 150px; display: flex; align-items: center; justify-content: center;
    border-bottom: 2px solid var(--band-line);
  }
  .contact-row .icon-cell svg { width: 26px; height: 26px; fill: #fff; }
  .contact-row .info {
    position: relative; flex: 1; background: var(--strip);
    padding: 10px 24px 0 44px;
    font-size: 19px; line-height: 24px; color: var(--text);
    border-right: 5px solid var(--accent);
  }
  .contact-row .info::before {
    content: ""; position: absolute; left: 0; top: 50%;
    transform: translateY(-50%);
    border-top: 10px solid transparent; border-bottom: 10px solid transparent;
    border-left: 12px solid var(--accent);
  }
  .contact-row.phone { --accent: var(--orange); }
  .contact-row.web { --accent: var(--blue); }
  .contact-row.place { --accent: var(--green); }
  .brand {
    position: absolute; left: 660px; top: 110px;
    display: flex; align-items: center; gap: 14px;
  }
  .brand .dot { width: 22px; height: 22px; border-radius: 50%; background: var(--leaf); flex: none; }
  .brand .wordmark {
    font-weight: 600; font-size: 26px; line-height: 1.15; color: var(--leaf);
  }
</style>
</head>
<body>
<main class="canvas">
  <article class="card">
    <div class="side-band"></div>

    <header class="identity">
      <h1 class="name">MAREN HOLT</h1>
      <p class="role">MANAGER</p>
    </header>

    <div class="brand">
      <span class="dot"></span>
      <span class="wordmark">Brambleway<br>Farming</span>
    </div>

    <section class="contacts">
      <div class="contact-row phone">
        <div class="icon-cell">
          <svg viewBox="0 0 24 24" aria-label="Phone"><path d="M6.6 10.8a15.1 15.1 0 0 0 6.6 6.6l2.2-2.2c.3-.3.7-.4 1-.2 1.1.4 2.3.6 3.6.6.6 0 1 .4 1 1V20c0 .6-.4 1-1 1A17 17 0 0 1 3 4c0-.6.4-1 1-1h3.5c.6 0 1 .4 1 1 0 1.3.2 2.5.6 3.6.1.3 0 .7-.2 1l-2.3 2.2z"/></svg>
        </div>
        <div class="info">250-555-0182<br>250-555-0183</div>
      </div>
      <div class="contact-row web">
        <div class="icon-cell">
          <svg viewBox="0 0 24 24" aria-label="Web" fill="none"><g fill="none" stroke="#fff" stroke-width="1.6"><circle cx="12" cy="12" r="9"/><ellipse cx="12" cy="12" rx="4" ry="9"/><path d="M3 12h18M4.5 7.5h15M4.5 16.5h15"/></g></svg>
        </div>
        <div class="info">hello@bramblewayfarm.ca<br>www.bramblewayfarm.ca</div>
      </div>
      <div class="contact-row place">
        <div class="icon-cell">
          <svg viewBox="0 0 24 24" aria-label="Location"><path d="M12 2a7 7 0 0 0-7 7c0 5.2 7 13 7 13s7-7.8 7-13a7 7 0 0 0-7-7zm0 9.5A2.5 2.5 0 1 1 12 6.5a2.5 2.5 0 0 1 0 5z"/></svg>
        </div>
        <div class="info">Orchard Lane, Glenmore,<br>Kelowna, BC V1V 2K3, CA</div>
      </div>
    </section>
  </article>
</main>
</body>
</html>
```